Business card for apparel company. Specializing in fishing and boating performance wear. Main company name is Marlow Pelican Company, LLC brand name for apparel is TIDEWAKE. See website www.TidewakeBayline.com I will attach some logos to consider.

```html
<!DOCTYPE html>
<html lang="en">
<head>
<meta charset="utf-8">
<title>Tidewake Business Card</title>
<link href="https://fonts.googleapis.com/css2?family=Montserrat:wght@400;500;700;800&display=swap" rel="stylesheet">
<style>
  :root {
    --page-bg: #e6e8eb;
    --back-slate: #3e4e60;
    --back-mint: #a9cbc6;
    --front-white: #ffffff;
    --brand-blue: #2f7fce;
    --name-blue: #1a9ee0;
    --text-grey: #3a3a3a;
    --wave-light: #19b4e8;
    --wave-deep: #2f5fb8;
  }
  * { margin: 0; padding: 0; box-sizing: border-box; }
  html, body { width: 1200px; height: 900px; overflow: hidden; }
  body {
    background: var(--page-bg);
    font-family: "Montserrat", sans-serif;
    position: relative;
  }
  .card {
    position: absolute;
    left: 250px;
    width: 700px;
    height: 400px;
    border-radius: 28px;
    overflow: hidden;
    box-shadow: 0 10px 30px rgba(0,0,0,0.18);
  }
  .card-back { top: 40px; background: var(--back-slate); }
  .card-front { top: 460px; background: var(--front-white); }

  .back-brand {
    position: absolute;
    inset: 0;
    display: flex;
    align-items: center;
    justify-content: center;
    gap: 18px;
  }
  .back-brand .brand-dot {
    width: 34px; height: 34px; border-radius: 50%;
    background: var(--back-mint);
  }
  .back-brand .brand-name {
    font-weight: 800;
    font-size: 68px;
    letter-spacing: 3px;
    color: var(--back-mint);
  }

  .front-wave { position: absolute; left: 0; top: 0; width: 700px; height: 400px; }

  .front-brand {
    position: absolute;
    left: 30px; top: 120px;
    width: 320px;
    display: flex;
    flex-direction: column;
    align-items: center;
    gap: 14px;
  }
  .front-brand .brand-dot {
    width: 54px; height: 54px; border-radius: 50%;
    background: var(--brand-blue);
  }
  .front-brand .brand-name {
    font-weight: 800;
    font-size: 48px;
    letter-spacing: 2px;
    color: var(--brand-blue);
  }

  .divider {
    position: absolute;
    left: 372px; top: 70px;
    width: 1.5px; height: 230px;
    background: var(--brand-blue);
  }

  .contact {
    position: absolute;
    left: 398px; top: 68px;
    color: var(--text-grey);
  }
  .contact .person-name {
    font-weight: 700;
    font-size: 27px;
    letter-spacing: 2px;
    color: var(--name-blue);
    line-height: 1.1;
  }
  .contact .person-role {
    font-size: 15px;
    margin: 4px 0 14px;
  }
  .contact-list { list-style: none; }
  .contact-list li {
    display: flex; align-items: center; gap: 10px;
    font-size: 15px;
    margin-bottom: 8px;
  }
  .contact-list svg { width: 15px; height: 15px; flex: none; }
  .address { font-size: 15px; line-height: 1.45; margin-top: 10px; }
</style>
</head>
<body>
  <section class="card card-back">
    <div class="back-brand">
      <span class="brand-dot"></span>
      <span class="brand-name">TIDEWAKE</span>
    </div>
  </section>

  <section class="card card-front">
    <svg class="front-wave" viewBox="0 0 700 400" aria-hidden="true">
      <defs>
        <linearGradient id="waveFill" x1="0" y1="0" x2="1" y2="0">
          <stop offset="0" stop-color="var(--wave-light)"/>
          <stop offset="0.6" stop-color="var(--wave-deep)"/>
          <stop offset="1" stop-color="var(--wave-light)"/>
        </linearGradient>
      </defs>
      <path d="M0,272 C140,340 400,318 700,392 L700,400 L0,400 Z" fill="url(#waveFill)"/>
      <path d="M0,256 C130,326 390,304 700,380" fill="none" stroke="var(--wave-deep)" stroke-width="2"/>
    </svg>

    <div class="front-brand">
      <span class="brand-dot"></span>
      <span class="brand-name">TIDEWAKE</span>
    </div>

    <div class="divider"></div>

    <div class="contact">
      <p class="person-name">CORIN VALE</p>
      <p class="person-role">CEO/Founder</p>
      <ul class="contact-list">
        <li>
          <svg viewBox="0 0 16 16"><path fill="var(--name-blue)" d="M4 1.5 6.3 4 5 5.6c.8 1.8 2.2 3.3 4 4.2L10.5 8.4 13 10.6 11.8 13C7 13 3 9 3 4.2Z"/></svg>
          (555) 410-2987
        </li>
        <li>
          <svg viewBox="0 0 16 16"><rect x="1" y="3" width="14" height="10" rx="1" fill="var(--name-blue)"/><path d="M1.5 3.8 8 9l6.5-5.2" fill="none" stroke="#fff" stroke-width="1.2"/></svg>
          info@TidewakeBayline.com
        </li>
        <li>
          <svg viewBox="0 0 16 16"><g fill="none" stroke="var(--name-blue)" stroke-width="1.3"><circle cx="8" cy="8" r="6.5"/><ellipse cx="8" cy="8" rx="2.8" ry="6.5"/><path d="M1.5 8h13M2.5 5h11M2.5 11h11"/></g></svg>
          www.TidewakeBayline.com
        </li>
      </ul>
      <p class="address">Po Box 4120 Harbor Lane<br>Region Name CD 7316</p>
    </div>
  </section>
</body>
</html>
```